Business Card Design

We need a business card design for a Executive search firm based in London & the North East called Kestrelby. We specialise in mid - snr level (£50k - £200k) IT placements. Our company colour is navy blue.

Target Market(s)

CEO, HR Director, Sales Director/VP - (35 - 50), well educated, British, European & American

Industry/Entity Type

Business

Contact Information for Business Card

Kestrelby Staffing Limited, Owen Caskell
Mobile - 0044 7731 482 616
London Office - Kestrelby House, 27 Fernmoor, Wexcombe. HA5 3LQ
Tel: 00 44 20 418 62093
North East Office – Velmora Centre, Ashgrove Way, Tillerby, NE41 2RD
Tel: 00 44 191 6842051
www.kestrelbystaffing-example.com

Also the same details for my Business Partner Ravi Tolani
with his mobile number as 0044 7852 307718

Requirements
Must have
• must have the same logo

the logo needs to be the same but made sharper

```html
<!DOCTYPE html>
<html lang="en">
<head>
<meta charset="utf-8">
<title>Kestrelby Business Card</title>
<link rel="stylesheet" href="https://fonts.googleapis.com/css2?family=Arimo:wght@400;700&display=swap">
<style>
  :root {
    --navy: #0d5599;
    --ink: #0b4f93;
    --paper: #ffffff;
    --backdrop-light: #eeeeee;
    --backdrop-dark: #cfcfcf;
  }
  * { margin: 0; padding: 0; box-sizing: border-box; }
  html, body { width: 1200px; height: 900px; overflow: hidden; }
  body {
    background: radial-gradient(ellipse at 50% 40%, var(--backdrop-light), var(--backdrop-dark));
    font-family: "Arimo", Arial, sans-serif;
    position: relative;
  }
  .card {
    position: absolute;
    top: 309px;
    width: 520px;
    height: 282px;
    border-radius: 22px;
    overflow: hidden;
    box-shadow: 0 6px 18px rgba(0,0,0,0.18);
  }
  .card-front {
    left: 50px;
    background: var(--navy);
    display: flex;
    align-items: center;
    justify-content: center;
  }
  .wordmark-front {
    color: var(--paper);
    font-size: 40px;
    font-weight: 400;
    letter-spacing: 0.5px;
  }
  .card-back {
    left: 630px;
    background: var(--paper);
    color: var(--ink);
  }
  .wordmark-back {
    position: absolute;
    left: 30px;
    top: 28px;
    font-size: 20px;
    font-weight: 400;
    color: var(--ink);
  }
  .holder {
    position: absolute;
    top: 76px;
    left: 0;
    right: 0;
    text-align: center;
  }
  .holder-name { font-size: 29px; font-weight: 700; }
  .holder-mobile { font-size: 14px; font-weight: 700; margin-top: 2px; }
  .offices {
    position: absolute;
    top: 147px;
    left: 36px;
    right: 20px;
    display: flex;
    gap: 32px;
  }
  .office { width: 220px; font-size: 11.5px; line-height: 15px; }
  .office-title { font-weight: 700; margin-bottom: 8px; }
  .office-row { display: flex; }
  .office-label { width: 60px; flex: none; }
  .office-value::before { content: ": "; }
  .office-value { white-space: pre-line; }
  .web-band {
    position: absolute;
    left: 0; right: 0; bottom: 0;
    height: 30px;
    background: var(--navy);
    color: var(--paper);
    font-size: 10.5px;
    display: flex;
    align-items: center;
    justify-content: center;
  }
</style>
</head>
<body>
  <section class="card card-front">
    <span class="wordmark-front">kestrelby</span>
  </section>

  <section class="card card-back">
    <span class="wordmark-back">kestrelby</span>
    <div class="holder">
      <div class="holder-name">Owen Caskell</div>
      <div class="holder-mobile">0044 7731 482 616</div>
    </div>
    <div class="offices">
      <div class="office">
        <div class="office-title">LONDON OFFICE</div>
        <div class="office-row"><span class="office-label">Address</span><span class="office-value">Kestrelby House
27 Fernmoor, Wexcombe.
HA5 3LQ</span></div>
        <div class="office-row"><span class="office-label">Phone</span><span class="office-value">00 44 20 418 62093</span></div>
      </div>
      <div class="office">
        <div class="office-title">NORTH EAST OFFICE</div>
        <div class="office-row"><span class="office-label">Address</span><span class="office-value">Velmora Centre
Ashgrove Way, Tillerby
NE41 2RD</span></div>
        <div class="office-row"><span class="office-label">Phone</span><span class="office-value">00 44 191 6842051</span></div>
      </div>
    </div>
    <div class="web-band">www.kestrelbystaffing-example.com</div>
  </section>
</body>
</html>
```